New Book Cover Design Project: Belly Balance and Calm Stomachs

5-1/2 x8-1/2 inch cover front and back, with spine for a 45,000-word book.
Title: Belly Balance and Calm Stomachs. Subtitle: Restore Your Inner Garden and Leave Behind Bloating Woes, Slow Energy, Mental Haze, Extra Pounds, and Swelling—for a Brighter, Lighter Self. Author: Mavis Thornquill. Thorough discussion of how to achieve good digestion and lifelong gut health mainly through a quality diet based on real food free of chemicals. Ten chapters. I am author of nine other books, focused on vibrant health through natural living. I'm looking for a simple and impactful cover. My most recent book, also with cover from Pixel Harbor, is The Lone Pantry Plan: Reshape Your Bond with Meals in Only 30 Days.

Target Market(s)

Mostly middle aged women who want to feel better and have real solutions for their digestion and gut problems, including less midriff fat

Industry/Entity Type

Self-help health information from a nutritionist and family health advocate.

Font styles to use
Serif

Colors

Designer to choose colors to be used in the design.

Requirements
Must have
• Some way to indicate the author is a woman, my name being Mavis Thornquill. Multicolored, upbeat, with some graphic reference to gut health but not with an illustration of microbes or intestinesnGra
Nice to have
• Perhaps an image of women's flat bellies or before and after images of flat bellies, or anything else suggestive of a smooth-functioning living systempas
Should not have
• See above.

```html
<!DOCTYPE html>
<html lang="en">
<head>
<meta charset="utf-8">
<title>Belly Balance and Calm Stomachs — Mavis Thornquill</title>
<link rel="stylesheet" href="https://fonts.googleapis.com/css2?family=Libre+Baskerville:ital,wght@0,400;0,700;1,400&family=Playfair+Display:wght@700;900&display=swap">
<style>
  :root {
    --teal: #106f97;
    --yellow: #ffe500;
    --white: #ffffff;
    --plum: #7d0b6b;
    --forest: #1f3114;
    --skin: #f8dcc8;
    --skin-light: #fdeee2;
    --cotton: #a9a9a6;
    --denim: #45617d;
    --leaf: #8fc35a;
    --leaf-pale: #b3d77c;
    --leaf-deep: #78b02a;
    --hair: #2b1a12;
    --suit: #efe6c6;
  }
  html, body { margin: 0; padding: 0; overflow: hidden; }
  body { width: 776px; height: 1200px; background: var(--white); }
  .cover { position: relative; width: 776px; height: 1200px; background: var(--teal); overflow: hidden; }

  .title-block { position: absolute; left: 0; top: 0; width: 776px; height: 350px; }
  .title-block text { font-family: "Playfair Display", serif; font-weight: 900; fill: var(--yellow); }

  .rule { position: absolute; background: var(--white); }
  .rule--top { left: 7px; top: 349px; width: 769px; height: 14px; }
  .rule--mid { left: 0; top: 622px; width: 776px; height: 14px; }
  .rule--low { left: 0; top: 805px; width: 776px; height: 14px; }

  .belly-photo {
    position: absolute; left: 0; top: 363px; width: 776px; height: 259px;
    background:
      linear-gradient(180deg, rgba(169,169,166,.9) 0%, rgba(169,169,166,0) 20%, rgba(69,97,125,0) 80%, rgba(69,97,125,.9) 100%),
      radial-gradient(ellipse 200px 150px at 212px 130px, var(--skin-light) 0%, var(--skin) 70%, rgba(248,220,200,0) 100%),
      radial-gradient(ellipse 160px 150px at 597px 130px, var(--skin-light) 0%, var(--skin) 70%, rgba(248,220,200,0) 100%),
      var(--forest);
  }

  .subtitle-band {
    position: absolute; left: 0; top: 652px; width: 776px; height: 139px;
    background: var(--plum);
  }
  .subtitle-band .tick { position: absolute; left: 32px; top: 46px; width: 68px; height: 64px; }
  .subtitle {
    position: absolute; left: 118px; top: 17px; margin: 0; width: 650px;
    font-family: "Libre Baskerville", serif; font-size: 28px; line-height: 34px;
    color: var(--white); white-space: nowrap;
  }

  .food-photo {
    position: absolute; left: 0; top: 819px; width: 776px; height: 320px;
    background:
      linear-gradient(180deg, rgba(120,176,42,0) 0%, rgba(120,176,42,0) 88%, var(--leaf-deep) 92%),
      radial-gradient(ellipse 260px 220px at 200px 120px, #c4d45e 0%, var(--leaf-pale) 60%, rgba(179,215,124,0) 100%),
      var(--leaf);
  }
  .author-photo {
    position: absolute; left: 450px; top: 805px; width: 326px; height: 395px;
    background:
      radial-gradient(ellipse 110px 120px at 175px 160px, #f1cdbd 0%, #e7b9a6 45%, rgba(43,26,18,0) 100%),
      radial-gradient(ellipse 170px 200px at 170px 170px, var(--hair) 0%, var(--hair) 60%, rgba(43,26,18,0) 100%),
      radial-gradient(ellipse 200px 120px at 175px 395px, var(--suit) 0%, var(--suit) 70%, rgba(239,230,198,0) 100%);
  }

  .tagline {
    position: absolute; left: 33px; top: 915px; margin: 0;
    font-family: "Libre Baskerville", serif; font-style: italic; font-size: 62px; line-height: 63px;
    color: var(--white); text-shadow: 0 2px 10px rgba(40, 60, 10, .6); white-space: nowrap;
  }
  .tagline span { display: block; }
  .tagline span + span { padding-left: 40px; }

  .author-bar {
    position: absolute; left: 0; top: 1139px; width: 464px; height: 61px; background: var(--teal);
  }
  .author {
    margin: 0; line-height: 64px; text-align: center;
    font-family: "Libre Baskerville", serif; font-weight: 700; font-size: 28px; letter-spacing: 5px;
    color: var(--white); white-space: nowrap;
  }
</style>
</head>
<body>
<main class="cover">
  <svg class="title-block" viewBox="0 0 776 350" aria-label="Belly Balance and Calm Stomachs">
    <defs>
      <filter id="title-glow" x="-10%" y="-20%" width="120%" height="140%">
        <feDropShadow dx="0" dy="2" stdDeviation="5" flood-color="#052c42" flood-opacity=".85"/>
      </filter>
    </defs>
    <g filter="url(#title-glow)">
      <text x="118" y="139" font-size="122" textLength="516" lengthAdjust="spacingAndGlyphs">BELLY BALANCE</text>
      <text x="322" y="204" font-size="54" textLength="147" lengthAdjust="spacingAndGlyphs">AND</text>
      <text x="40" y="325" font-size="124" textLength="711" lengthAdjust="spacingAndGlyphs">CALM STOMACHS</text>
    </g>
  </svg>

  <div class="rule rule--top"></div>
  <div class="belly-photo" role="img" aria-label="Before and after photo of a woman's midriff: a rounded belly beside a flat toned belly, grey tops above and blue jeans below, on a dark green background"></div>
  <div class="rule rule--mid"></div>

  <section class="subtitle-band">
    <svg class="tick" viewBox="0 0 68 64" aria-hidden="true">
      <path d="M0 34 L22 63 L68 0 L22 46 Z" fill="var(--yellow)"/>
    </svg>
    <p class="subtitle">Restore Your Inner Garden and Leave<br>Behind Bloating Woes, Slow Energy,<br>Mental Haze, Extra Pounds, and Swelling</p>
  </section>

  <div class="rule rule--low"></div>
  <div class="food-photo" role="img" aria-label="Green-tinted photo of a plate of quinoa, roasted vegetables, broccoli and carrots with a fork"></div>
  <div class="author-photo" role="img" aria-label="Portrait of the author, a smiling woman with dark curly hair in a cream jacket and gold necklace"></div>
  <p class="tagline"><span>for a Brighter,</span><span>Lighter Self.</span></p>

  <div class="author-bar">
    <p class="author">MAVIS THORNQUILL</p>
  </div>
</main>
</body>
</html>
```